Kettle Ledger Business Card design

We need a stand out business card design for Accounting practice based in Australia specialising in pubs, clubs and hotels. We help venues maximise margins, create time and manage cashflow. One club we have been working with for the last 6 months has increased revenue by 3% and margin by 5% in this time frame. We have a back office outsourced system that costs less than having a full time employee and also allows the venues the added benefit of:<br/>-using the office space to become a revenue generating opportunity. <br/>-a complete system to enhance governance, accountability and efficiency within their operation<br/>-52 weeks cover so no hassle to cover annual/sick .. leave<br/><br/>We would like to see designs that use the colours of our logo (green & blue).
Target Market(s)
Australian Pubs, Clubs & Hotels abookkeeping, accounting and tax services
Industry/Entity Type
Accountant
Contact Information for Business Card
Miriam Oakley CPA
Principal
Accountant Tax Agent
Miriam@KettleLedger-example.com.au
0418693142
www.kettleledger-example.com.au
Accounting / Payroll / Tax / SMSF / Technology
Colors
Designer to choose colors to be used in the design.
Look and feel
Each slider illustrates characteristics of the customer's brand and the style your logo design should communicate.

```html
<!DOCTYPE html>
<html lang="en">
<head>
<meta charset="utf-8">
<title>Kettle Ledger Business Card</title>
<link rel="stylesheet" href="https://fonts.googleapis.com/css2?family=Poppins:wght@600;700&family=Roboto:wght@400&display=swap">
<style>
  :root {
    --page-bg: #e9eaec;
    --brand-blue: #24398f;
    --brand-blue-soft: #2a45a8;
    --brand-green: #11723b;
    --paper: #ffffff;
    --text-blue: #24398f;
    --divider: #5b6cae;
  }
  * { box-sizing: border-box; margin: 0; padding: 0; }
  html, body {
    width: 1200px; height: 1124px; overflow: hidden;
    background: var(--page-bg);
  }
  .sheet {
    width: 1200px; height: 1124px;
    display: flex; flex-direction: column; align-items: center;
    gap: 24px; padding-top: 36px;
  }
  .card {
    position: relative;
    width: 900px; height: 514px;
    border-bottom: 4px solid var(--brand-green);
    box-shadow: 0 6px 18px rgba(0,0,0,.18);
    overflow: hidden;
  }

  /* Front */
  .card-front { background: var(--brand-blue); }
  .front-mark {
    position: absolute; left: 40px; top: 150px;
    width: 380px; height: 360px;
  }
  .front-brand {
    position: absolute; left: 450px; top: 150px;
    font-family: "Poppins", sans-serif; font-weight: 700;
    font-size: 56px; line-height: 1; color: var(--paper);
    letter-spacing: -0.5px; white-space: nowrap;
  }
  .front-services {
    position: absolute; left: 452px; top: 236px;
    font-family: "Poppins", sans-serif; font-weight: 600;
    font-size: 21px; line-height: 1.5; color: var(--paper);
    white-space: nowrap;
  }
  .front-services .sep { opacity: .85; padding: 0 6px; font-weight: 400; }

  /* Back */
  .card-back { background: var(--paper); }
  .back-brand {
    position: absolute; left: 84px; top: 222px;
    display: flex; align-items: center; gap: 14px;
  }
  .back-brand .dot {
    width: 48px; height: 48px; border-radius: 50%;
    background: var(--brand-green);
  }
  .back-brand .name {
    font-family: "Poppins", sans-serif; font-weight: 700;
    font-size: 40px; line-height: 1; color: var(--brand-blue);
    white-space: nowrap;
  }
  .divider {
    position: absolute; left: 470px; top: 140px;
    width: 2px; height: 232px; background: var(--divider);
  }
  .person {
    position: absolute; left: 506px; top: 140px;
    font-family: "Roboto", sans-serif; color: var(--text-blue);
  }
  .person-name {
    font-family: "Poppins", sans-serif; font-weight: 700;
    font-size: 28px; color: var(--brand-green); line-height: 1.1;
    white-space: nowrap;
  }
  .person-role { font-size: 20px; line-height: 1.25; margin-top: 4px; }
  .contacts { list-style: none; margin-top: 22px; }
  .contacts li {
    display: flex; align-items: center; gap: 12px;
    font-size: 18px; line-height: 1.7; white-space: nowrap;
  }
  .contacts svg { width: 17px; height: 17px; flex: none; }
</style>
</head>
<body>
<main class="sheet">
  <section class="card card-front" aria-label="Card front">
    <svg class="front-mark" viewBox="0 0 380 360" role="img" aria-label="Faint embossed brand emblem area">
      <defs>
        <radialGradient id="markGlow" cx="55%" cy="55%" r="55%">
          <stop offset="0" stop-color="#2a45a8"/>
          <stop offset="1" stop-color="#24398f"/>
        </radialGradient>
      </defs>
      <circle cx="190" cy="190" r="165" fill="url(#markGlow)"/>
    </svg>
    <div class="front-brand">Kettle Ledger</div>
    <p class="front-services">
      Accounting<span class="sep">|</span>Payroll<span class="sep">|</span>Technology<br>
      Tax<span class="sep">|</span>SMSF
    </p>
  </section>

  <section class="card card-back" aria-label="Card back">
    <div class="back-brand">
      <span class="dot" aria-hidden="true"></span>
      <span class="name">Kettle Ledger</span>
    </div>
    <div class="divider" aria-hidden="true"></div>
    <div class="person">
      <h1 class="person-name">Miriam Oakley CPA</h1>
      <p class="person-role">Principal<br>Accountant Tax Agent</p>
      <ul class="contacts">
        <li>
          <svg viewBox="0 0 24 24" aria-hidden="true"><path fill="#11723b" d="M6.6 10.8a15.1 15.1 0 0 0 6.6 6.6l2.2-2.2c.3-.3.7-.4 1-.2 1.1.4 2.3.6 3.6.6.6 0 1 .4 1 1V20c0 .6-.4 1-1 1A17 17 0 0 1 3 4c0-.6.4-1 1-1h3.5c.6 0 1 .4 1 1 0 1.3.2 2.5.6 3.6.1.3 0 .7-.2 1z"/></svg>
          0418693142
        </li>
        <li>
          <svg viewBox="0 0 24 24" aria-hidden="true"><rect x="2.5" y="5" width="19" height="14" rx="1.5" fill="none" stroke="#11723b" stroke-width="2"/><path d="M3 6l9 7 9-7" fill="none" stroke="#11723b" stroke-width="2"/></svg>
          Miriam@KettleLedger-example.com.au
        </li>
        <li>
          <svg viewBox="0 0 24 24" aria-hidden="true"><g fill="none" stroke="#11723b" stroke-width="2"><circle cx="12" cy="12" r="9.5"/><ellipse cx="12" cy="12" rx="4.5" ry="9.5"/><path d="M2.5 12h19M4 7h16M4 17h16"/></g></svg>
          www.kettleledger-example.com.au
        </li>
      </ul>
    </div>
  </section>
</main>
</body>
</html>
```